Professional Business Cards for Recruiting Company

We'd like professional 2-sided business cards that reflect a color scheme that matches our website, www.queryvantline.com, and / or logo that is attached.

Slogan used is "We Know People", but needs to be editable because we change it up to "We Know Developers", "We Speak Geek", etc.

Must includes logo, slogan, first and last name, address, email, mobile number and website address.

Files attached for ideas.

Thanks!

Contact Information for Business Card

Logo, Company name, First name, Last name, addresss, email, phone, website address.

Font styles to use
Sans Serif

Colors
0054AA
0677BA
7BADD7
CADEEF
E8F1F8

Requirements
Nice to have
• I do like the following designs. 22962062 and 22962651. Couple ideas anyway.

```html
<!DOCTYPE html>
<html lang="en">
<head>
<meta charset="utf-8">
<title>Queryvant Business Cards</title>
<link href="https://fonts.googleapis.com/css2?family=Poppins:wght@300;400;500&display=swap" rel="stylesheet">
<style>
  :root {
    --stage: #262626;
    --brand-deep: #1f4f8f;
    --brand: #0054aa;
    --brand-mid: #0677ba;
    --brand-light: #7badd7;
    --paper: #ffffff;
    --ink: #1c1c1c;
    --muted: #6d6d6d;
  }
  * { box-sizing: border-box; margin: 0; padding: 0; }
  html, body { width: 1200px; height: 1015px; overflow: hidden; }
  body {
    background: var(--stage);
    font-family: "Poppins", sans-serif;
    position: relative;
  }
  .card {
    position: absolute;
    left: 300px;
    width: 600px;
    height: 343px;
    box-shadow: 0 12px 30px rgba(0,0,0,.45);
  }
  /* Front */
  .card-front { top: 110px; background: var(--brand-deep); overflow: hidden; }
  .card-front .pattern {
    position: absolute; inset: 0;
    background: linear-gradient(135deg, #2a63ad 0%, #1f4f8f 50%, #173f74 100%);
  }
  .front-brand {
    position: absolute; inset: 0;
    display: flex; flex-direction: column; align-items: center; justify-content: center; gap: 14px;
  }
  .brand-square {
    width: 42px; height: 42px; border: 2px solid var(--paper);
  }
  .front-brand .brand-name {
    color: var(--paper); font-weight: 300; font-size: 34px; letter-spacing: 3px;
  }
  /* Back */
  .card-back { top: 560px; background: var(--paper); }
  .back-brand {
    position: absolute; left: 40px; top: 150px;
    display: flex; align-items: center; gap: 12px;
  }
  .back-brand .brand-square {
    width: 40px; height: 40px; border: 2px solid var(--brand);
  }
  .back-brand .brand-name {
    color: var(--brand); font-weight: 300; font-size: 30px; letter-spacing: 1px; line-height: 1;
  }
  .brand-tagline {
    margin-top: 4px; padding-top: 3px; border-top: 1.5px solid var(--brand);
    font-size: 6.5px; font-weight: 500; letter-spacing: 1px; color: var(--muted); text-transform: uppercase;
  }
  .divider {
    position: absolute; left: 318px; top: 95px; width: 1px; height: 150px; background: var(--ink);
  }
  .contact { position: absolute; left: 338px; top: 58px; }
  .person-name {
    font-size: 19px; letter-spacing: .5px; line-height: 1.1;
    border-left: 1.5px solid var(--brand); padding-left: 10px; margin-left: -14px;
  }
  .person-name .first { color: var(--brand); }
  .person-name .last { color: var(--muted); }
  .person-title { font-size: 11px; color: var(--ink); letter-spacing: .5px; margin-bottom: 12px; }
  .contact-list { list-style: none; font-size: 13px; color: var(--ink); line-height: 1.5; }
  .contact-list li { display: flex; align-items: center; gap: 6px; }
  .contact-list svg { width: 12px; height: 12px; fill: var(--brand); flex: none; }
  .address { margin-top: 10px; margin-left: 18px; font-size: 13px; line-height: 1.3; color: var(--ink); }
  .slogan {
    position: absolute; left: 0; right: 0; bottom: 38px; padding-left: 190px;
    font-size: 20px; color: var(--brand); letter-spacing: .5px; text-align: center;
  }
</style>
</head>
<body>
  <section class="card card-front">
    <div class="pattern" role="img" aria-label="Repeating embossed brand-mark pattern in blue tones"></div>
    <div class="front-brand">
      <span class="brand-square"></span>
      <span class="brand-name">QUERYVANT</span>
    </div>
  </section>

  <section class="card card-back">
    <div class="back-brand">
      <span class="brand-square"></span>
      <div>
        <div class="brand-name">QUERYVANT</div>
        <div class="brand-tagline">Professional Sourcing and Recruiting</div>
      </div>
    </div>

    <div class="divider"></div>

    <div class="contact">
      <div class="person-name"><span class="first">MARCUS</span> <span class="last">DELANO</span></div>
      <div class="person-title">MANAGING DIRECTOR</div>
      <ul class="contact-list">
        <li><svg viewBox="0 0 24 24"><path d="M6.6 10.8a15 15 0 0 0 6.6 6.6l2.2-2.2a1 1 0 0 1 1-.25 11.4 11.4 0 0 0 3.6.57 1 1 0 0 1 1 1V20a1 1 0 0 1-1 1A17 17 0 0 1 3 4a1 1 0 0 1 1-1h3.5a1 1 0 0 1 1 1c0 1.25.2 2.45.57 3.6a1 1 0 0 1-.25 1z"/></svg>044-987 650 312</li>
        <li><svg viewBox="0 0 24 24"><path d="M2 5h20v14H2z M2 5l10 8 10-8" fill="none" stroke="#0054aa" stroke-width="2.5"/></svg>info@queryvantline.com</li>
        <li><svg viewBox="0 0 24 24"><circle cx="12" cy="12" r="10" fill="none" stroke="#0054aa" stroke-width="2"/><path d="M2 12h20M12 2c3 3 3 17 0 20M12 2c-3 3-3 17 0 20" fill="none" stroke="#0054aa" stroke-width="1.6"/></svg>www.queryvantline.com</li>
      </ul>
      <div class="address">17, Harbor Lane Suite 4<br>60218, Country Name</div>
    </div>

    <div class="slogan">WE KNOW PEOPLE</div>
  </section>
</body>
</html>
```